brivox new business card design project

we need a new business card design. you can view info about us @ brivox.com. i have attached an example of our previous card with our previous name that we no longer use. We really liked the design, colors etc. look below to see more info about this project. it asks for a limited number of words. please see our website for more info about our compnay.

Target Market(s)

law enforcement

Contact Information for Business Card

i have uploaded an example of what we used before that we liked.

Font styles to use
Serif

```html
<!DOCTYPE html>
<html lang="en">
<head>
<meta charset="utf-8">
<title>Brivox Business Card</title>
<link rel="stylesheet" href="https://fonts.googleapis.com/css2?family=Open+Sans:wght@400;700&family=Raleway:wght@200&display=swap">
<style>
  :root {
    --page-bg: #2a2c30;
    --navy-dark: #0d2a3f;
    --navy: #1d5472;
    --stripe-blue: #1f4f8a;
    --stripe-grey: #9ea3a8;
    --band-grey: #c9cbcd;
    --ink: #1a1a1a;
    --ink-soft: #6b6e72;
    --name-blue: #163e5c;
    --paper: #ffffff;
  }
  * { margin: 0; padding: 0; box-sizing: border-box; }
  html, body { width: 1200px; height: 900px; overflow: hidden; }
  body {
    background: var(--page-bg);
    display: flex;
    align-items: center;
    justify-content: center;
    gap: 40px;
    font-family: "Open Sans", sans-serif;
  }
  .card {
    position: relative;
    width: 540px;
    height: 310px;
    border-radius: 22px;
    overflow: hidden;
  }
  .card-front { background: var(--paper); }
  .front-shapes { position: absolute; inset: 0; }
  .wordmark {
    font-family: "Raleway", sans-serif;
    font-weight: 200;
    letter-spacing: 4px;
    color: var(--ink);
  }
  .card-front .wordmark {
    position: absolute;
    top: 26px;
    left: 40px;
    font-size: 50px;
  }
  .person {
    position: absolute;
    top: 112px;
    left: 96px;
  }
  .person-name {
    font-weight: 700;
    font-size: 19px;
    color: var(--name-blue);
  }
  .person-title {
    font-size: 11.5px;
    color: var(--ink-soft);
  }
  .divider {
    position: absolute;
    top: 170px;
    left: 250px;
    width: 1px;
    height: 100px;
    background: linear-gradient(to bottom, transparent, #c8c8c8, transparent);
  }
  .contact-list {
    position: absolute;
    top: 166px;
    left: 268px;
    list-style: none;
    font-size: 15px;
    color: var(--ink-soft);
    line-height: 1.3;
  }
  .contact-list li { display: flex; gap: 8px; align-items: flex-start; }
  .contact-icon {
    flex: none;
    width: 16px;
    height: 16px;
    margin-top: 2px;
    background: var(--stripe-grey);
    border-radius: 2px;
    display: flex;
    align-items: center;
    justify-content: center;
  }
  .card-back {
    background: radial-gradient(ellipse at 60% 55%, var(--navy) 0%, var(--navy-dark) 100%);
  }
  .card-back .wordmark {
    position: absolute;
    top: 108px;
    width: 100%;
    text-align: center;
    font-size: 62px;
    color: #f2f4f6;
  }
  .web-band {
    position: absolute;
    left: 0; right: 0; bottom: 0;
    height: 44px;
    background: linear-gradient(to bottom, #e3e4e5, var(--band-grey));
    display: flex;
    align-items: center;
    padding-left: 34px;
    font-size: 18px;
    font-weight: 700;
    color: var(--navy-dark);
  }
</style>
</head>
<body>
  <article class="card card-front">
    <svg class="front-shapes" width="540" height="310" viewBox="0 0 540 310">
      <polygon points="0,150 0,310 160,310" fill="var(--navy)"/>
      <polyline points="0,138 172,310" stroke="var(--stripe-grey)" stroke-width="9" fill="none"/>
      <polyline points="0,124 186,310" stroke="var(--stripe-blue)" stroke-width="3" fill="none"/>
      <polygon points="540,70 540,310 420,310" fill="var(--navy)"/>
      <polyline points="540,56 406,310" stroke="var(--stripe-grey)" stroke-width="9" fill="none"/>
      <polyline points="540,40 390,310" stroke="var(--stripe-blue)" stroke-width="3" fill="none"/>
    </svg>
    <div class="wordmark">BRIVOX</div>
    <div class="person">
      <div class="person-name">Daniel Hartwell</div>
      <div class="person-title">Founder/chief Executive Officer</div>
    </div>
    <div class="divider"></div>
    <ul class="contact-list">
      <li>
        <span class="contact-icon"><svg width="10" height="10" viewBox="0 0 10 10"><path d="M5 0a3.5 3.5 0 0 0-3.5 3.5C1.5 6 5 10 5 10s3.5-4 3.5-6.5A3.5 3.5 0 0 0 5 0zm0 5a1.4 1.4 0 1 1 0-2.8A1.4 1.4 0 0 1 5 5z" fill="#fff"/></svg></span>
        <span>4215 Linden Park Road<br>Austin, TX 78745</span>
      </li>
      <li>
        <span class="contact-icon"><svg width="10" height="10" viewBox="0 0 10 10"><path d="M2 0.5l2 2-1 1.2a6 6 0 0 0 3.3 3.3l1.2-1 2 2-1.3 1.5C4.5 9.5 0.5 5.5 0.5 1.8z" fill="#fff"/></svg></span>
        <span>555.214.7730</span>
      </li>
      <li>
        <span class="contact-icon"><svg width="10" height="10" viewBox="0 0 10 10"><rect x="0.5" y="2" width="9" height="6" fill="#fff"/><path d="M0.5 2l4.5 3.5L9.5 2" stroke="var(--stripe-grey)" fill="none"/></svg></span>
        <span>info@brivox.com</span>
      </li>
      <li>
        <span class="contact-icon"><svg width="10" height="10" viewBox="0 0 10 10"><circle cx="5" cy="5" r="4" stroke="#fff" fill="none"/><path d="M1 5h8M5 1c-2 2.5-2 5.5 0 8M5 1c2 2.5 2 5.5 0 8" stroke="#fff" fill="none" stroke-width="0.8"/></svg></span>
        <span>www.brivox.com</span>
      </li>
    </ul>
  </article>

  <article class="card card-back">
    <div class="wordmark">BRIVOX</div>
    <div class="web-band">www.brivox.com</div>
  </article>
</body>
</html>
```